Redesign our business card for more impact

We want to completely replace the back design of our card, and refresh or even change the front entirely. We are happy with our black K4 logo and do not want to change it.
Our company address changed too. It is now 2307 Larkmoor, Irvine, CA 92741
Updates

It was reported by Art Harbor email today that the uploaded files didnt upload. I am trying again.

Target Market(s)

Architects and Building Owners (People making multi-million dollar decisions)

Industry/Entity Type

Consulting Engineering

Contact Information for Business Card

Contact info on the front. "wallpaper" design on back with tag line on the back "Engineering Your Future"

Font styles to use
Sans Serif

Requirements
Must have
• A vivid, modern, impactful ...but tasteful back of card design. It should communicate our premier status, but grab attention as innovative. DESIGN SHOULD BE ELEGANT AND NOT TOO BUSY.
Nice to have
• Repeating pattern, multi-color, something creative...
Should not have
• Anything that looks too playful or that we are not serious professionals. It should also not be too boring or conservative.

```html
<!DOCTYPE html>
<html lang="en">
<head>
<meta charset="utf-8">
<title>K4 Business Card</title>
<link rel="stylesheet" href="https://fonts.googleapis.com/css2?family=Noto+Sans:wght@400;700&family=Barlow:wght@500&display=swap">
<style>
  :root {
    --backdrop: #ababab;
    --card-top: #005e92;
    --card-mid: #007a8a;
    --card-bottom: #008a80;
    --ink-light: #ffffff;
    --text-font: "Noto Sans", Arial, sans-serif;
    --tagline-font: "Barlow", Arial, sans-serif;
  }
  * { margin: 0; padding: 0; box-sizing: border-box; }
  html, body {
    width: 1200px;
    height: 1000px;
    overflow: hidden;
    background: var(--backdrop);
  }
  .stage {
    position: relative;
    width: 1200px;
    height: 1000px;
  }
  .card {
    position: absolute;
    width: 615px;
    height: 354px;
    color: var(--ink-light);
    font-family: var(--text-font);
    overflow: hidden;
  }
  .card-surface {
    position: absolute;
    inset: 0;
    background: linear-gradient(180deg, var(--card-top) 0%, var(--card-mid) 40%, var(--card-bottom) 100%);
  }
  .card--front { left: 101px; top: 135px; }
  .card--back { left: 479px; top: 545px; }

  .wordmark {
    position: absolute;
    font-family: var(--text-font);
    font-weight: 700;
    color: var(--ink-light);
    line-height: 1;
    letter-spacing: -0.02em;
  }
  .card--front .wordmark {
    left: 0;
    right: 0;
    top: 122px;
    text-align: center;
    font-size: 104px;
  }
  .tagline {
    position: absolute;
    left: 0;
    right: 0;
    top: 269px;
    text-align: center;
    font-family: var(--tagline-font);
    font-weight: 500;
    font-size: 16px;
    letter-spacing: 0.22em;
  }
  .card--back .wordmark {
    left: 38px;
    top: 49px;
    font-size: 54px;
  }
  .contact {
    position: absolute;
    right: 54px;
    top: 137px;
    text-align: right;
    font-size: 17px;
    line-height: 22px;
  }
  .contact-name,
  .contact-role {
    font-weight: 700;
    letter-spacing: 0.06em;
    text-transform: uppercase;
  }
  .contact-lines { margin-top: 22px; }
  .contact-address { margin-top: 22px; }
</style>
</head>
<body>
<main class="stage">
  <section class="card card--front">
    <div class="card-surface" role="img" aria-label="Blue to teal gradient with a faint repeating triangle pattern"></div>
    <div class="wordmark">K4</div>
    <p class="tagline">ENGINEERING YOUR FUTURE</p>
  </section>

  <section class="card card--back">
    <div class="card-surface" role="img" aria-label="Blue to teal gradient with a faint repeating triangle pattern"></div>
    <div class="wordmark">K4</div>
    <div class="contact">
      <p class="contact-name">Dana Whitfield</p>
      <p class="contact-role">CEO</p>
      <div class="contact-lines">
        <p>(555) 318-4072</p>
        <p>dana.whitfield@k4eng.com</p>
        <p>www.k4eng.com</p>
      </div>
      <p class="contact-address">2307 Larkmoor, Irvine, CA 92741</p>
    </div>
  </section>
</main>
</body>
</html>
```